New UK IT business
Business cards etc
Project: New UK IT business
New UK IT business - Environment
Creative Brief
Bright & Fun-filled
Cobalt Harvest Limited or Ltd - Gordon Pressey
Director
14 Brindle Lane Oakhurst Trading Park Fenwick Cross Herts HP9 3QL United Kingdom
gord@cobaltharvest-example.com
www.cobaltharvest-example.com
please do one card for Gord Pressey - Director and one for Rosalind Pressey - Director and one for Company - with no name
full colour - simple logo and website address only for the inside of the card i want it to have the fold on the horizontal meaning 55mm down the front with logo and name and address details the back as described above the inside I would like a picture of business people and have the messages of Redundant IT and Computer equipment Business people - corporate business people wanted All UK areas please suggest what you think and design around it thanks I will be available to answer questions when i see some designs for inspiration

```html
<!DOCTYPE html>
<html lang="en">
<head>
<meta charset="utf-8">
<title>Cobalt Harvest – Business Cards</title>
<link href="https://fonts.googleapis.com/css2?family=Open+Sans:ital,wght@0,400;0,600;0,700;0,800;1,400&display=swap" rel="stylesheet">
<style>
  :root {
    --backdrop: #e8dccb;
    --card: #ffffff;
    --ink: #1c1c1c;
    --muted: #3a3a3a;
    --brand-green: #3d8f2a;
    --rule: #8a8a8a;
  }
  * { box-sizing: border-box; margin: 0; padding: 0; }
  html, body {
    width: 1200px;
    height: 751px;
    overflow: hidden;
  }
  body {
    background: var(--backdrop);
    font-family: "Open Sans", Arial, sans-serif;
    color: var(--ink);
    position: relative;
  }
  .icon-defs { position: absolute; width: 0; height: 0; }

  .card-sheet {
    position: absolute;
    inset: 0;
    display: grid;
    grid-template-columns: 500px 500px;
    grid-template-rows: repeat(3, 210px);
    column-gap: 104px;
    row-gap: 20px;
    padding: 40px 0 0 48px;
  }

  .business-card {
    background: var(--card);
    box-shadow: 0 2px 6px rgba(0,0,0,0.25);
    display: flex;
    flex-direction: column;
    padding: 18px 24px 8px;
  }

  .card-header {
    display: flex;
    align-items: center;
    justify-content: space-between;
    gap: 24px;
    height: 56px;
    padding-bottom: 8px;
    border-bottom: 2px dotted var(--rule);
  }

  .brand {
    display: flex;
    align-items: center;
    gap: 10px;
    flex: none;
  }
  .brand-dot {
    width: 40px;
    height: 40px;
    border-radius: 50%;
    background: var(--brand-green);
    flex: none;
  }
  .brand-name {
    font-weight: 800;
    font-size: 22px;
    letter-spacing: 0.3px;
    color: var(--brand-green);
    text-transform: uppercase;
    line-height: 1;
    white-space: nowrap;
  }

  .holder { text-align: center; white-space: nowrap; }
  .holder-name {
    font-weight: 700;
    font-size: 18px;
    line-height: 1.15;
  }
  .holder-role {
    font-size: 10.5px;
    font-style: italic;
    color: var(--muted);
  }

  .card-body {
    display: flex;
    padding-top: 12px;
    font-size: 11px;
    line-height: 17px;
  }
  .contact-list {
    list-style: none;
    width: 262px;
    flex: none;
  }
  .contact-list li {
    display: flex;
    align-items: center;
    gap: 5px;
    white-space: nowrap;
  }
  .contact-label { font-weight: 700; width: 14px; }
  .contact-icon {
    width: 12px;
    height: 12px;
    fill: var(--brand-green);
    flex: none;
  }
  .address {
    font-style: italic;
    color: var(--muted);
    white-space: nowrap;
  }

  .card-footer {
    margin-top: auto;
    border-top: 2px dotted var(--rule);
    text-align: center;
    font-size: 10.5px;
    font-weight: 600;
    padding-top: 4px;
  }
</style>
</head>
<body>

<svg class="icon-defs" aria-hidden="true">
  <defs>
    <symbol id="icon-phone" viewBox="0 0 24 24">
      <path d="M6.6 10.8c1.4 2.8 3.8 5.1 6.6 6.6l2.2-2.2c.3-.3.7-.4 1-.2 1.1.4 2.3.6 3.6.6.6 0 1 .4 1 1V20c0 .6-.4 1-1 1C10.6 21 3 13.4 3 4c0-.6.4-1 1-1h3.5c.6 0 1 .4 1 1 0 1.3.2 2.5.6 3.6.1.3 0 .7-.2 1l-2.3 2.2z"/>
    </symbol>
    <symbol id="icon-mobile" viewBox="0 0 24 24">
      <path d="M7 1h10c1.1 0 2 .9 2 2v18c0 1.1-.9 2-2 2H7c-1.1 0-2-.9-2-2V3c0-1.1.9-2 2-2zm0 3v14h10V4H7zm5 15.5a1.2 1.2 0 1 0 0 2.4 1.2 1.2 0 0 0 0-2.4z"/>
    </symbol>
    <symbol id="icon-fax" viewBox="0 0 24 24">
      <path d="M6 2h12v6H6zM3 9h18c1.1 0 2 .9 2 2v7h-4v4H5v-4H1v-7c0-1.1.9-2 2-2zm4 7v4h10v-4H7z"/>
    </symbol>
    <symbol id="icon-mail" viewBox="0 0 24 24">
      <path d="M2 5h20v14H2V5zm2 2v.5l8 5 8-5V7H4zm0 2.8V17h16V9.8l-8 5-8-5z"/>
    </symbol>
  </defs>
</svg>

<main class="card-sheet">

  <article class="business-card">
    <header class="card-header">
      <div class="brand"><span class="brand-dot"></span><span class="brand-name">Cobalt Harvest</span></div>
    </header>
    <section class="card-body">
      <ul class="contact-list">
        <li><span class="contact-label">P:</span>0808 555 0142</li>
        <li><span class="contact-label">M:</span>07700 900 318</li>
        <li><span class="contact-label">F:</span>0808 555 0177</li>
        <li><span class="contact-label">E:</span>info@cobaltharvest-example.com</li>
      </ul>
      <address class="address">14 Brindle Lane<br>Oakhurst Trading Park<br>Fenwick Cross Herts<br>HP9 3QL United Kingdom</address>
    </section>
    <footer class="card-footer">www.cobaltharvest-example.com</footer>
  </article>

  <article class="business-card">
    <header class="card-header">
      <div class="brand"><span class="brand-dot"></span><span class="brand-name">Cobalt Harvest</span></div>
    </header>
    <section class="card-body">
      <ul class="contact-list">
        <li><svg class="contact-icon"><use href="#icon-phone"/></svg>0808 555 0142</li>
        <li><svg class="contact-icon"><use href="#icon-mobile"/></svg>07700 900 318</li>
        <li><svg class="contact-icon"><use href="#icon-fax"/></svg>0808 555 0177</li>
        <li><svg class="contact-icon"><use href="#icon-mail"/></svg>info@cobaltharvest-example.com</li>
      </ul>
      <address class="address">14 Brindle Lane<br>Oakhurst Trading Park<br>Fenwick Cross Herts<br>HP9 3QL United Kingdom</address>
    </section>
    <footer class="card-footer">www.cobaltharvest-example.com</footer>
  </article>

  <article class="business-card">
    <header class="card-header">
      <div class="brand"><span class="brand-dot"></span><span class="brand-name">Cobalt Harvest</span></div>
      <div class="holder"><p class="holder-name">Rosalind Pressey</p><p class="holder-role">Director</p></div>
    </header>
    <section class="card-body">
      <ul class="contact-list">
        <li><span class="contact-label">P:</span>0808 555 0142</li>
        <li><span class="contact-label">M:</span>07700 900 318</li>
        <li><span class="contact-label">F:</span>0808 555 0177</li>
        <li><span class="contact-label">E:</span>rosalind@cobaltharvest-example.com</li>
      </ul>
      <address class="address">14 Brindle Lane<br>Oakhurst Trading Park<br>Fenwick Cross Herts<br>HP9 3QL United Kingdom</address>
    </section>
    <footer class="card-footer">www.cobaltharvest-example.com</footer>
  </article>

  <article class="business-card">
    <header class="card-header">
      <div class="brand"><span class="brand-dot"></span><span class="brand-name">Cobalt Harvest</span></div>
      <div class="holder"><p class="holder-name">Rosalind Pressey</p><p class="holder-role">Director</p></div>
    </header>
    <section class="card-body">
      <ul class="contact-list">
        <li><svg class="contact-icon"><use href="#icon-phone"/></svg>0808 555 0142</li>
        <li><svg class="contact-icon"><use href="#icon-mobile"/></svg>07700 900 318</li>
        <li><svg class="contact-icon"><use href="#icon-fax"/></svg>0808 555 0177</li>
        <li><svg class="contact-icon"><use href="#icon-mail"/></svg>rosalind@cobaltharvest-example.com</li>
      </ul>
      <address class="address">14 Brindle Lane<br>Oakhurst Trading Park<br>Fenwick Cross Herts<br>HP9 3QL United Kingdom</address>
    </section>
    <footer class="card-footer">www.cobaltharvest-example.com</footer>
  </article>

  <article class="business-card">
    <header class="card-header">
      <div class="brand"><span class="brand-dot"></span><span class="brand-name">Cobalt Harvest</span></div>
      <div class="holder"><p class="holder-name">Gord Pressey</p><p class="holder-role">Director</p></div>
    </header>
    <section class="card-body">
      <ul class="contact-list">
        <li><span class="contact-label">P:</span>0808 555 0142</li>
        <li><span class="contact-label">M:</span>07700 900 318</li>
        <li><span class="contact-label">F:</span>0808 555 0177</li>
        <li><span class="contact-label">E:</span>gord@cobaltharvest-example.com</li>
      </ul>
      <address class="address">14 Brindle Lane<br>Oakhurst Trading Park<br>Fenwick Cross Herts<br>HP9 3QL United Kingdom</address>
    </section>
    <footer class="card-footer">www.cobaltharvest-example.com</footer>
  </article>

  <article class="business-card">
    <header class="card-header">
      <div class="brand"><span class="brand-dot"></span><span class="brand-name">Cobalt Harvest</span></div>
      <div class="holder"><p class="holder-name">Gord Pressey</p><p class="holder-role">Director</p></div>
    </header>
    <section class="card-body">
      <ul class="contact-list">
        <li><svg class="contact-icon"><use href="#icon-phone"/></svg>0808 555 0142</li>
        <li><svg class="contact-icon"><use href="#icon-mobile"/></svg>07700 900 318</li>
        <li><svg class="contact-icon"><use href="#icon-fax"/></svg>0808 555 0177</li>
        <li><svg class="contact-icon"><use href="#icon-mail"/></svg>gord@cobaltharvest-example.com</li>
      </ul>
      <address class="address">14 Brindle Lane<br>Oakhurst Trading Park<br>Fenwick Cross Herts<br>HP9 3QL United Kingdom</address>
    </section>
    <footer class="card-footer">www.cobaltharvest-example.com</footer>
  </article>

</main>
</body>
</html>
```